Volra Beer Logo/Label Design For Beer Bottles

I need a logo/label design for my beer!

I brew my own beer and I already have a name and a logo/label idea that I would like you to turn into something awesome

My beer is called Volra, an old Greek town (now a part of Turkey) where Saint Corvan once performed miracles that would eventually make him the saint of beer (more info: https://en.lorepedix.example/wiki/Volra)

I thought about a logo/label that has Saint Corvan (something like this picture http://www.st-corvan-parish.example/images/icons/IMG_1321b.jpg)

One of his hands is gesturing just like the picture above. The other one is wrapped around one of those little crosses that have a small string that you normally put around your neck, and that same hand is holding my beer.

I would like the beer to have the same logo on it, but instead of Volra written on it, it should say Βόλρα (just check on Lorepedix for the Ancient Greek way of writing it)

So, long story short, I want a logo/label for my beer bottles. The label must have Saint Corvan drawn, with a friendly face, one hand gesturing and the other one wrapped in a little cross holding my beer which also happens to have the same logo but with a different way of writing the name of the beer.

Remember to write Volra on the logo/label. You can write it on top or on the bottom of Saint Corvan (like this https://cdn.folioshelf.example/project_modules/disp/f6bd2538725649.5606991f9448a.png or this https://cdn.craftlessonhub.example/vector/uploads/legacy/tuts/128_Beer_Label/Picture%2031.jpg). I would like it to be cheerful and friendly, without losing its ancient history/tradition feeling to it. Gotta stay classy, even though it is a drawing.

Try different fonts and colors, as longs as they stick to the main objective

Target Market(s)

Adults who love craft beer, history and tradition

Logo Text

Volra

Font styles to use
Serif
Decorative
Script

Requirements
Must have
• Beer label design for my bottles! So it must have (of course) the name of the beer. Saint Corvan, the hand gesture, the little cross and a beer bottle with the same label on his hand
Nice to have
• Maybe, when you write Volra, paint it in gold or yellow. Just a MAYBE, a suggestion, it can probably be much cooler in another color. Also, be advised that it is a India Pale Ale. If you are thinking about writing the type of the beer (which is not required), that is what you should write
Should not have
• Beer written next to Volra. Just write Volra. It doesn't need to be Volra Beer

```html
<!DOCTYPE html>
<html lang="en">
<head>
<meta charset="utf-8">
<title>Volra — Premium Lager Label</title>
<link rel="stylesheet" href="https://fonts.googleapis.com/css2?family=Playfair+Display:ital,wght@0,700;1,600&display=swap">
<style>
  :root {
    --backdrop: #ece5e6;
    --gold-light: #f3d06a;
    --gold: #d9a21c;
    --gold-deep: #a8760c;
    --rim: #f6dc8c;
    --wine: #7a1d12;
    --robe-red: #a8321c;
    --robe-gold: #d7a742;
    --cream: #f8ecd0;
  }
  * { margin: 0; padding: 0; box-sizing: border-box; }
  html, body { width: 1200px; height: 886px; overflow: hidden; }
  body {
    background: var(--backdrop);
    font-family: "Playfair Display", Georgia, serif;
    position: relative;
  }
  .label {
    position: absolute;
    left: 250px;
    top: 143px;
    width: 400px;
    height: 600px;
    border-radius: 50% / 34%;
    background: radial-gradient(ellipse at 45% 40%, var(--gold-light), var(--gold) 55%, var(--gold-deep));
    border: 6px solid var(--rim);
    box-shadow: inset 0 0 0 3px var(--gold-deep);
  }
  .label__art {
    position: absolute;
    left: 70px;
    top: 40px;
    width: 248px;
    height: 330px;
    border-radius: 124px 124px 24px 24px;
    background: linear-gradient(180deg, var(--robe-gold) 0%, var(--cream) 30%, var(--robe-red) 62%, #6e1e10 100%);
  }
  .wordmark {
    position: absolute;
    left: 0;
    width: 100%;
    text-align: center;
    color: var(--wine);
    font-weight: 700;
    line-height: 1;
  }
  .wordmark__name { display: block; }
  .wordmark__swash { display: block; margin: 0 auto; }
  .wordmark__type {
    display: block;
    font-style: italic;
    font-weight: 600;
  }
  .label .wordmark { top: 380px; }
  .label .wordmark__name { font-size: 84px; }
  .label .wordmark__type { font-size: 24px; margin-top: 2px; }
  .standalone {
    position: absolute;
    left: 700px;
    top: 360px;
    width: 300px;
    height: 180px;
  }
  .standalone .wordmark { top: 0; }
  .standalone .wordmark__name { font-size: 92px; }
  .standalone .wordmark__type { font-size: 26px; margin-top: 2px; }
</style>
</head>
<body>
  <main class="label">
    <div class="label__art" role="img" aria-label="Illustration of Saint Corvan in red and gold robes with a halo, one hand raised in blessing, the other holding a small cross and a bottle of Volra beer"></div>
    <div class="wordmark">
      <span class="wordmark__name">Βόλρα</span>
      <svg class="wordmark__swash" width="300" height="16" viewBox="0 0 300 16">
        <path d="M6 4 Q150 20 294 4" fill="none" stroke="var(--wine)" stroke-width="4" stroke-linecap="round"/>
      </svg>
      <span class="wordmark__type">Premium Lager</span>
    </div>
  </main>

  <section class="standalone">
    <div class="wordmark">
      <span class="wordmark__name">Βόλρα</span>
      <svg class="wordmark__swash" width="300" height="16" viewBox="0 0 300 16">
        <path d="M6 4 Q150 20 294 4" fill="none" stroke="var(--wine)" stroke-width="4" stroke-linecap="round"/>
      </svg>
      <span class="wordmark__type">Premium Lager</span>
    </div>
  </section>
</body>
</html>
```